Pale Meadow Distillery
Exceptional Handcrafted Spirits
Designers, I want to personally thank all of you for your help and support on Pale Meadow Distillery. It was a close tie amongst many of you. In the end I had a very difficult time choosing a winner. Please keep up the good work and look for my next project to start later next week. You guys are awesome!!!
All, please let me know what other files I can get you so that the word "distillery" appears correct. Some of you are having to remove the word from the barrels and it leaves a blank spot. I can try and get you any of the original corel draw (cdr) files from the logo designer.
The two fonts used in my logo are Goudy Old Style and PassionConflictROB.
All designers, I am looking for a one side business card.
could you please upload ai or eps file of logo

```html
<!DOCTYPE html>
<html lang="en">
<head>
<meta charset="utf-8">
<title>Pale Meadow Distillery — Stationery</title>
<link rel="stylesheet" href="https://fonts.googleapis.com/css2?family=Sorts+Mill+Goudy&display=swap">
<style>
  :root {
    --paper: #ffffff;
    --backdrop: #ffffff;
    --ink: #1f1f1f;
    --accent-red: #c4161c;
    --flap: #2a2a2a;
    --edge: #d8d8d8;
    --shadow: rgba(0,0,0,0.18);
  }
  * { margin: 0; padding: 0; box-sizing: border-box; }
  html, body {
    width: 1200px; height: 681px; overflow: hidden;
    background: var(--backdrop);
    font-family: "Sorts Mill Goudy", Georgia, serif;
    color: var(--ink);
  }
  .canvas { position: relative; width: 1200px; height: 681px; }
  .sheet {
    position: absolute; background: var(--paper);
    border: 1px solid var(--edge);
    box-shadow: 1px 2px 4px var(--shadow);
    overflow: hidden;
  }
  .wordmark {
    position: absolute; display: flex; align-items: center; gap: 6px;
    color: var(--ink); white-space: nowrap; line-height: 1;
  }
  .wordmark .dot {
    border-radius: 50%; border: 2px solid var(--ink); flex: none;
  }
  .rule-set { position: absolute; left: 0; right: 0; }
  .rule-set span { display: block; }
  .rule-black { background: var(--ink); }
  .rule-red { background: var(--accent-red); }
  .small-caps { font-variant: small-caps; letter-spacing: 0.5px; }

  /* envelope front */
  .envelope-front { left: 60px; top: 96px; width: 480px; height: 216px; }
  .envelope-front .wordmark { left: 16px; top: 30px; font-size: 22px; }
  .envelope-front .wordmark .dot { width: 20px; height: 20px; }
  .envelope-front .rule-set { top: 110px; left: 10px; right: 10px; }
  .envelope-front .return-address { position: absolute; left: 16px; top: 145px; font-size: 10px; }

  /* envelope back */
  .envelope-back { left: 60px; top: 360px; width: 480px; height: 216px; }
  .envelope-back svg { position: absolute; left: 0; top: 0; }
  .envelope-back .flap-web {
    position: absolute; left: 0; right: 0; top: 62px; text-align: center;
    color: var(--paper); font-size: 9px;
  }

  /* letterhead */
  .letterhead { left: 619px; top: 53px; width: 365px; height: 600px; }
  .letterhead .wordmark { left: 0; right: 0; justify-content: center; top: 58px; font-size: 21px; }
  .letterhead .wordmark .dot { width: 18px; height: 18px; }
  .letterhead .rule-set { top: 114px; left: 8px; right: 8px; }
  .letterhead .contact {
    position: absolute; left: 0; right: 0; top: 132px; text-align: center;
    font-size: 8.5px; line-height: 13px;
  }

  /* business card */
  .business-card { left: 972px; top: 444px; width: 216px; height: 120px; }
  .business-card .wordmark { left: 8px; top: 12px; font-size: 12px; gap: 4px; }
  .business-card .wordmark .dot { width: 11px; height: 11px; border-width: 1.5px; }
  .business-card .rule-set { top: 36px; left: 5px; right: 5px; }
  .business-card .card-name {
    position: absolute; left: 10px; top: 48px; font-size: 7px; color: var(--accent-red);
  }
  .business-card .card-title { position: absolute; left: 10px; top: 57px; font-size: 5.5px; }
  .business-card .card-details {
    position: absolute; right: 10px; bottom: 10px; text-align: right;
    font-size: 5.5px; line-height: 7.5px;
  }
</style>
</head>
<body>
<main class="canvas">

  <section class="sheet envelope-front" aria-label="Envelope front">
    <div class="wordmark"><span class="dot"></span>Pale Meadow Distillery</div>
    <div class="rule-set">
      <span class="rule-black" style="height:3px"></span>
      <span style="height:2px"></span>
      <span class="rule-red" style="height:3px"></span>
      <span style="height:2px"></span>
      <span class="rule-black" style="height:1px"></span>
    </div>
    <p class="return-address small-caps">118 W Harbor Lane, Ashford, NC 28790</p>
  </section>

  <section class="sheet envelope-back" aria-label="Envelope back">
    <svg width="480" height="216" viewBox="0 0 480 216">
      <polygon points="0,0 480,0 470,132 10,132" fill="var(--flap)"/>
    </svg>
    <p class="flap-web small-caps">palemeadowdistillery.com</p>
  </section>

  <section class="sheet letterhead" aria-label="Letterhead">
    <div class="wordmark"><span class="dot"></span>Pale Meadow Distillery</div>
    <div class="rule-set">
      <span class="rule-black" style="height:3px"></span>
      <span style="height:2px"></span>
      <span class="rule-red" style="height:3px"></span>
      <span style="height:2px"></span>
      <span class="rule-black" style="height:1px"></span>
    </div>
    <div class="contact small-caps">
      <p>118 W Harbor Lane, Ashford, NC 28790</p>
      <p>Phone: 828.555.0142 | Fax: 828.555.0187 | www.palemeadowdistillery.com</p>
    </div>
  </section>

  <section class="sheet business-card" aria-label="Business card">
    <div class="wordmark"><span class="dot"></span>Pale Meadow Distillery</div>
    <div class="rule-set">
      <span class="rule-black" style="height:1.5px"></span>
      <span style="height:1px"></span>
      <span class="rule-red" style="height:1.5px"></span>
      <span style="height:1px"></span>
      <span class="rule-black" style="height:0.5px"></span>
    </div>
    <p class="card-name">Karl Brusby</p>
    <p class="card-title">Master Distiller</p>
    <div class="card-details small-caps">
      <p>118 W Harbor Lane, Ashford, NC 28790</p>
      <p>Phone: 828.555.0142 | Fax: 828.555.0187</p>
      <p>www.palemeadowdistillery.com</p>
    </div>
  </section>

</main>
</body>
</html>
```